Zephyr Quill - Dog Supplement Brand

Here a link to a word doc with all of my info.
Please read it carefully.
https://files.brindlemoor.net/page/d/7tRkWpLzQ2mNvA84xHcYbEuJ0sFdKo93Tg5LhPq-2/view?ref=open
Its 2 pages. Home Page and Product Page.
Oh and btw: the poses I attached dont have a shadow, so it would be good if you added a shadow to the poses .
If you have any questions please let me know.
Target Market(s)
Dog Owners In UK
Industry/Entity Type
Dog supplements
Number of Pages Required
2 page
Requirements
Must have
- Home page and product page files. Super Hero Theme.

```html
<!DOCTYPE html>
<html lang="en">
<head>
<meta charset="utf-8">
<title>Zephyr Quill – Dog Supplements</title>
<link rel="stylesheet" href="https://fonts.googleapis.com/css2?family=Rubik:wght@400;500;600;700&family=Poppins:wght@300;400;500;600&display=swap">
<style>
:root{
  --orange:#fe8c3c;
  --coral:#fe6a3d;
  --red:#f9553f;
  --blue:#3e8bfc;
  --yellow:#fec52e;
  --green:#8bc34a;
  --teal:#4fd1a0;
  --purple:#7b6be6;
  --ink:#363b4e;
  --text:#5b6070;
  --white:#ffffff;
}
*{box-sizing:border-box;margin:0;padding:0}
html,body{width:1200px;height:4649px;overflow:hidden;background:var(--white)}
body{font-family:'Poppins',sans-serif;color:var(--text)}
.page{position:relative;width:1200px;height:4649px;overflow:hidden}
.abs{position:absolute}
.shapes{position:absolute;left:0;top:0}
h1,h2,h3,h4,.heading{font-family:'Rubik',sans-serif;font-weight:500;color:var(--ink)}
.ph{position:absolute}

/* header */
.site-header{position:absolute;left:0;top:0;width:1200px;height:78px;background:var(--white);z-index:5}
.menu-icon{position:absolute;left:172px;top:30px;width:20px}
.menu-icon span{display:block;height:2px;background:var(--ink);margin-bottom:5px}
.brand{position:absolute;left:0;width:1200px;top:22px;text-align:center;font-family:'Rubik',sans-serif;font-weight:700;font-size:26px;color:var(--ink);letter-spacing:.5px}
.header-icons{position:absolute;right:170px;top:28px;display:flex;gap:24px}

/* buttons */
.pill{position:absolute;display:flex;align-items:center;border-radius:20px;font-family:'Rubik',sans-serif;font-weight:600;font-size:11px;letter-spacing:2px;text-transform:uppercase}
.pill .dot{position:absolute;right:2px;top:2px;border-radius:50%;display:flex;align-items:center;justify-content:center}
.pill-white{background:var(--white);color:var(--ink)}
.pill-white .dot{background:var(--coral)}
.pill-red{background:var(--red);color:var(--white)}
.pill-red .dot{background:var(--white);border:2px solid var(--red)}

/* hero */
.hero-text{position:absolute;left:171px;top:212px;color:var(--white);font-family:'Rubik',sans-serif}
.hero-text .l1{font-size:25px;font-weight:400;line-height:34px}
.hero-text .l2{font-size:34px;font-weight:400;line-height:48px}
.hero-text .l3{font-size:46px;font-weight:600;line-height:54px}

/* about */
.about-hi{left:606px;top:812px;font-family:'Rubik',sans-serif;font-size:26px;color:var(--ink)}
.about-title{left:606px;top:838px;font-size:50px;font-weight:600}
.about-copy{left:606px;top:906px;width:410px;font-size:13.5px;line-height:26px;color:var(--text)}

/* offer */
.section-title{position:absolute;left:0;width:1200px;text-align:center;font-family:'Rubik',sans-serif;font-weight:600;font-size:46px}
.offer-title{top:1428px;color:var(--white)}
.offer-card{position:absolute;width:268px;height:181px;background:var(--white);border-radius:14px}
.offer-card .label{position:absolute;left:0;right:0;bottom:18px;text-align:center;font-family:'Rubik',sans-serif;font-weight:500;font-size:16px;color:var(--ink)}
.offer-dog{position:absolute;border-radius:45% 45% 30% 30%}

/* products */
.product-title{top:2253px;color:var(--ink)}
.product-card{position:absolute;width:268px;height:170px;background:var(--white);border-radius:14px;box-shadow:0 10px 28px rgba(40,40,70,.12);text-align:center}
.product-card .name{position:absolute;left:0;right:0;top:110px;font-family:'Rubik',sans-serif;font-size:14px;color:var(--ink)}
.product-card .price{position:absolute;left:0;right:0;top:134px;font-family:'Rubik',sans-serif;font-size:14px;color:var(--text)}
.bottle{position:absolute;width:130px;height:170px;border-radius:16px 16px 10px 10px;background:linear-gradient(180deg,#f3f4f6 0,#f3f4f6 16%,#4caf3b 16%,#7bd04a 55%,#e2332e 80%,#f5f5f5 100%)}

/* testimonials */
.love-title{top:2813px;color:var(--ink)}
.testimonial{position:absolute;left:235px;top:2951px;width:731px;height:265px;background:var(--white);box-shadow:0 10px 34px rgba(40,40,70,.10)}
.t-name{position:absolute;left:180px;top:28px;font-family:'Rubik',sans-serif;font-weight:500;font-size:16px;color:var(--ink)}
.t-date{position:absolute;left:180px;top:52px;font-size:10px;font-style:italic;color:#9a9eab}
.t-copy{position:absolute;left:180px;top:88px;width:470px;font-size:13.5px;line-height:26px}
.arrow-btn{position:absolute;width:30px;height:30px;border-radius:50%;background:var(--red);display:flex;align-items:center;justify-content:center}

/* vets */
.vets-title{left:171px;top:3448px;font-family:'Rubik',sans-serif;font-weight:600;font-size:48px;line-height:56px;color:#e6ecff}
.video{position:absolute;left:532px;top:3330px;width:497px;height:316px;background:#111}
.video .frame{position:absolute;left:0;top:0;width:497px;height:290px;background:radial-gradient(ellipse at 55% 55%,#f3c68a 0,#b17b47 35%,#5a3a26 75%,#2f2219 100%)}
.video .bar{position:absolute;left:0;bottom:0;width:497px;height:26px;background:#1b1b1b;display:flex;align-items:center;gap:10px;padding:0 10px}

/* why */
.why-title{left:170px;top:3728px;font-size:46px;font-weight:600;line-height:52px;color:var(--ink)}
.feature{position:absolute;top:3704px;width:190px;height:126px;background:var(--white);box-shadow:0 8px 24px rgba(40,40,70,.10);padding:28px 18px 0}
.feature .icon{width:40px;height:34px;border-radius:6px;background:linear-gradient(135deg,#ffd37a,#f36a3a)}
.feature .label{margin-top:10px;font-family:'Rubik',sans-serif;font-size:13.5px;line-height:20px;color:var(--ink);font-weight:500}

/* regulated */
.reg-title{left:170px;top:3962px;font-size:44px;font-weight:600;color:var(--ink);white-space:nowrap;z-index:2}
.reg-copy{left:171px;top:4036px;width:470px;font-size:13.5px;line-height:26px}
.badge{position:absolute;top:4131px;width:62px;height:62px;border-radius:50%;border:3px solid #c9ccd4;background:#f4f5f7}

/* footer */
.footer{position:absolute;left:0;top:4305px;width:1200px;height:344px;background:var(--ink)}
.f-col{position:absolute;top:62px}
.f-col h4{font-family:'Rubik',sans-serif;font-size:14px;font-weight:500;color:var(--white);padding-bottom:12px;border-bottom:1px solid #555a6c;width:193px}
.f-col ul{list-style:none;margin-top:14px}
.f-col li{font-size:13px;color:#c8cbd6;height:36px;line-height:20px}
.email{position:absolute;left:760px;top:126px;width:267px;height:38px;background:var(--white);border-radius:4px;font-size:12px;color:#9a9eab;padding:10px 12px}
.subscribe{position:absolute;left:908px;top:171px;width:119px;height:35px;background:var(--red);border-radius:4px;color:var(--white);font-family:'Rubik',sans-serif;font-weight:600;font-size:11px;letter-spacing:2px;text-align:center;line-height:35px}
.copyright{position:absolute;left:171px;top:307px;font-size:11px;color:#c8cbd6}
.copyright b{color:var(--yellow);font-weight:400}
.cards{position:absolute;left:794px;top:302px;display:flex;gap:14px}
.cards span{width:38px;height:24px;border-radius:3px;background:var(--white);font-family:'Poppins',sans-serif;font-size:7.5px;font-weight:500;color:var(--ink);text-align:center;line-height:24px}
</style>
</head>
<body>
<div class="page">

  <svg class="shapes" width="1200" height="4649" viewBox="0 0 1200 4649" aria-hidden="true">
    <path d="M0 78H1200V520C1050 560 900 560 760 640C620 720 420 610 260 640C140 660 60 700 0 725Z" fill="var(--orange)"/>
    <path d="M560 78H1200V520C1100 600 980 690 840 690C700 690 620 600 660 500C700 400 560 380 540 280C520 200 560 120 560 78Z" fill="var(--coral)"/>
    <circle cx="0" cy="572" r="42" fill="var(--white)"/>
    <circle cx="706" cy="646" r="38" fill="var(--orange)"/>
    <path d="M0 1100C200 1060 420 1090 560 1170C800 1260 960 1240 1010 1100C1050 980 1110 860 1200 830V2132H0Z" fill="var(--blue)"/>
    <circle cx="560" cy="1312" r="38" fill="var(--yellow)"/>
    <path d="M0 2250C150 2330 420 2360 460 2520C500 2700 200 2760 0 2830Z" fill="var(--yellow)"/>
    <circle cx="126" cy="2756" r="42" fill="var(--green)"/>
    <rect x="267" y="2902" width="103" height="356" fill="var(--teal)"/>
    <path d="M0 3274H1200V3520C1000 3560 820 3540 660 3600C520 3650 430 3640 330 3610C220 3580 100 3560 0 3560Z" fill="var(--purple)"/>
    <circle cx="446" cy="3623" r="33" fill="var(--yellow)"/>
    <path d="M1200 3800C1100 3830 1000 3900 960 4000C920 4120 820 4220 700 4305H1200Z" fill="var(--orange)"/>
  </svg>

  <header class="site-header">
    <div class="menu-icon"><span></span><span></span><span></span></div>
    <div class="brand">Zephyr Quill</div>
    <div class="header-icons">
      <svg width="14" height="14" viewBox="0 0 14 14"><circle cx="6" cy="6" r="4.5" fill="none" stroke="#363b4e" stroke-width="2"/><line x1="9.5" y1="9.5" x2="13" y2="13" stroke="#363b4e" stroke-width="2"/></svg>
      <svg width="14" height="14" viewBox="0 0 14 14"><circle cx="7" cy="4" r="3" fill="none" stroke="#363b4e" stroke-width="1.6"/><path d="M1.5 13.5C2 9.5 12 9.5 12.5 13.5" fill="none" stroke="#363b4e" stroke-width="1.6"/></svg>
      <svg width="14" height="14" viewBox="0 0 14 14"><path d="M2 5H12L11 13.5H3Z" fill="#363b4e"/><path d="M4.5 5V3.5A2.5 2.5 0 0 1 9.5 3.5V5" fill="none" stroke="#363b4e" stroke-width="1.5"/></svg>
    </div>
  </header>

  <section class="hero">
    <div class="hero-text">
      <div class="l1">Join Forces With Zephyr</div>
      <div class="l2">Quill &amp; Let Him Be Your</div>
      <div class="l3">Beloved Dog's Hero!</div>
    </div>
    <div class="pill pill-white" style="left:171px;top:368px;width:154px;height:36px;padding-left:24px">Join Forces
      <span class="dot" style="width:32px;height:32px"><svg width="14" height="10" viewBox="0 0 14 10"><path d="M1 5H12M8 1L12 5L8 9" fill="none" stroke="#fff" stroke-width="1.6"/></svg></span>
    </div>
    <div class="ph" role="img" aria-label="Supplement bottle beside the superhero husky mascot giving a thumbs up" style="left:632px;top:90px;width:380px;height:480px;border-radius:40% 40% 20% 20%;background:linear-gradient(160deg,#f4f4f6 0,#d8d9df 45%,#c2242a 70%,#2a2a30 100%);opacity:.92"></div>
  </section>

  <section class="about">
    <div class="ph" role="img" aria-label="Flying superhero husky mascot with a red cape" style="left:190px;top:785px;width:370px;height:334px;border-radius:46%;background:radial-gradient(circle at 55% 45%,#f2f3f5 0,#cfd1d8 45%,#d33a2c 75%,#f8f8f8 100%)"></div>
    <div class="abs about-hi">Hi! I'm</div>
    <h2 class="abs about-title">Zephyr Quill!</h2>
    <p class="abs about-copy">Lorem ipsum dolor sit amet, consectetur adipiscing elit. Fusce massa nisi, rhoncus ut ultrices in, consequat at velit. Suspendisse non neque viverra orci convallis facilisis. Fusce sodales quam sed neque vehicula pulvinar. Etiam eget aliquet arcu. Morbi varius, sapien nec egestas egestas.</p>
    <div class="pill pill-red" style="left:612px;top:1085px;width:152px;height:36px;padding-left:22px">Read More
      <span class="dot" style="width:32px;height:32px;top:2px"><svg width="14" height="10" viewBox="0 0 14 10"><path d="M1 5H12M8 1L12 5L8 9" fill="none" stroke="#f9553f" stroke-width="1.6"/></svg></span>
    </div>
  </section>

  <section class="offer">
    <h2 class="section-title offer-title">Here's what I offer</h2>

    <div class="offer-card" style="left:171px;top:1599px"><div class="label">Zephyr Quill Calm</div></div>
    <div class="offer-card" style="left:466px;top:1599px"><div class="label">Zephyr Quill Joint Support</div></div>
    <div class="offer-card" style="left:760px;top:1599px"><div class="label">Zephyr Quill MultiVits</div></div>
    <div class="offer-card" style="left:171px;top:1888px"><div class="label">Zephyr Quill Omega 369</div></div>
    <div class="offer-card" style="left:466px;top:1888px"><div class="label">Zephyr QuillProbiotics</div></div>
    <div class="offer-card" style="left:760px;top:1888px"><div class="label">Zephyr Quill Digestive Support</div></div>

    <div class="offer-dog" role="img" aria-label="Small fluffy dog in a patterned pyjama" style="left:230px;top:1505px;width:150px;height:225px;background:linear-gradient(180deg,#c99a68 0,#b98558 40%,#6f9fc0 70%,#e5c45a 100%)"></div>
    <div class="offer-dog" role="img" aria-label="Golden retriever sitting with a rose" style="left:540px;top:1498px;width:120px;height:235px;background:linear-gradient(180deg,#d9a56a 0,#c88d52 60%,#b87a44 100%)"></div>
    <div class="offer-dog" role="img" aria-label="French bulldog in a yellow shirt" style="left:830px;top:1498px;width:130px;height:232px;background:linear-gradient(180deg,#bfa999 0,#9e8878 45%,#f2b51c 70%,#d89c12 100%)"></div>
    <div class="offer-dog" role="img" aria-label="Beagle sitting" style="left:235px;top:1822px;width:140px;height:196px;background:linear-gradient(180deg,#8a5a32 0,#c58a52 40%,#f4f1ec 75%,#e9e3da 100%)"></div>
    <div class="offer-dog" role="img" aria-label="Cavalier spaniel lying down" style="left:490px;top:1860px;width:220px;height:150px;background:linear-gradient(90deg,#f3efe9 0,#a96a3c 40%,#f3efe9 100%)"></div>
    <div class="offer-dog" role="img" aria-label="Sheltie sitting" style="left:830px;top:1814px;width:130px;height:212px;background:linear-gradient(180deg,#7a4e2a 0,#b8824c 45%,#f4efe6 80%,#e8e2d8 100%)"></div>
  </section>

  <section class="products">
    <h2 class="section-title product-title">Zephyr Quill!</h2>
    <div class="product-card" style="left:171px;top:2469px"><div class="name">120 chicken flavor tablets</div><div class="price">£39.95</div></div>
    <div class="product-card" style="left:466px;top:2469px"><div class="name">120 chicken flavor tablets</div><div class="price">£39.95</div></div>
    <div class="product-card" style="left:760px;top:2469px"><div class="name">120 chicken flavor tablets</div><div class="price">£39.95</div></div>
    <div class="bottle" role="img" aria-label="Zephyr Quill Multivits bottle" style="left:240px;top:2379px"></div>
    <div class="bottle" role="img" aria-label="Zephyr Quill Multivits bottle" style="left:535px;top:2379px"></div>
    <div class="bottle" role="img" aria-label="Zephyr Quill Multivits bottle" style="left:829px;top:2379px"></div>
    <div class="pill pill-red" style="left:540px;top:2687px;width:136px;height:35px;padding-left:28px">View All
      <span class="dot" style="width:31px;height:31px"><svg width="14" height="10" viewBox="0 0 14 10"><path d="M1 5H12M8 1L12 5L8 9" fill="none" stroke="#f9553f" stroke-width="1.6"/></svg></span>
    </div>
  </section>

  <section class="love">
    <h2 class="section-title love-title">People Love Me</h2>
    <div class="testimonial">
      <div class="ph" role="img" aria-label="Portrait of a smiling customer in a grey sweater" style="left:23px;top:6px;width:136px;height:236px;background:linear-gradient(180deg,#eef0f2 0,#d9b48a 30%,#9a9ca3 60%,#7d8088 100%)"></div>
      <div class="t-name">Mara Ellison</div>
      <div class="t-date">January 11,2022</div>
      <p class="t-copy">Lorem ipsum dolor sit amet, consectetur adipiscing elit. Sed varius condimentum nisi, aliquet luctus est scue a. Suspendisse volutpat feugiat quam, a lobortis urna suscipit a. Donec rhoncus in urna et lacinia. Curabitur elit justo, rutrum sit amet sem ac, suscipit maximus quam.</p>
    </div>
    <div class="arrow-btn" style="left:175px;top:3064px"><svg width="12" height="10" viewBox="0 0 12 10"><path d="M11 5H1M5 1L1 5L5 9" fill="none" stroke="#fff" stroke-width="1.6"/></svg></div>
    <div class="arrow-btn" style="left:998px;top:3064px"><svg width="12" height="10" viewBox="0 0 12 10"><path d="M1 5H11M7 1L11 5L7 9" fill="none" stroke="#fff" stroke-width="1.6"/></svg></div>
  </section>

  <section class="vets">
    <h2 class="abs vets-title">Approved by<br>Expert Vets</h2>
    <div class="video">
      <div class="frame" role="img" aria-label="Golden retriever puppy running across a sunlit field"></div>
      <div class="bar">
        <svg width="14" height="14" viewBox="0 0 14 14"><path d="M3 2L12 7L3 12Z" fill="#fff"/></svg>
        <span style="font-size:8px;color:#fff;background:#333;padding:0 3px">00:51</span>
        <span style="flex:1;height:4px;background:#555;position:relative"><span style="position:absolute;left:0;top:0;width:12%;height:4px;background:#3ab8f0"></span></span>
        <span style="font-size:9px;color:#3ab8f0;font-weight:600">HD</span>
        <span style="font-size:10px;color:#fff;font-weight:600">Vidora</span>
      </div>
    </div>
  </section>

  <section class="why">
    <h2 class="abs why-title">Why<br>Choose Me?</h2>
    <div class="feature" style="left:442px"><div class="icon" role="img" aria-label="Organic leaves icon"></div><div class="label">Only Organic &amp; Natural Ingredients</div></div>
    <div class="feature" style="left:641px"><div class="icon" role="img" aria-label="Group of members icon"></div><div class="label">20% Off for all Zephyr Quill Squad Member</div></div>
    <div class="feature" style="left:839px"><div class="icon" role="img" aria-label="Delivery truck icon"></div><div class="label">Free Next Day UK Delivery</div></div>
  </section>

  <section class="regulated">
    <div class="ph" role="img" aria-label="Husky mascot in a lab coat holding a test tube" style="left:664px;top:3853px;width:238px;height:380px;border-radius:40% 40% 25% 25%;background:linear-gradient(180deg,#2c2c33 0,#f0c23a 18%,#e8e9ee 40%,#c9cbd3 85%,#2c2c33 100%)"></div>
    <h2 class="abs reg-title">Regulated &amp; Certified</h2>
    <p class="abs reg-copy">Lorem ipsum dolor sit amet, consectetur adipiscing elit. Fusce massa nisi, rhoncus ut ultrices in, consequat at velit. Suspendisse non neque viverra orci convallis facilisis. Fusce sodal</p>
    <div class="badge" style="left:169px"></div>
    <div class="badge" style="left:236px;border-color:#8bc34a"></div>
    <div class="badge" style="left:305px"></div>
  </section>

  <footer class="footer">
    <div class="f-col" style="left:171px"><h4>Useful Links</h4><ul><li>Join Zephyr Quill</li><li>Browse Supplements</li><li>About Zephyr Quill</li><li>Reviews</li><li>Need Help?</li></ul></div>
    <div class="f-col" style="left:476px"><h4>Other Links</h4><ul><li>My Account</li><li>My Cart</li><li>Privacy Policy</li><li>Search</li><li>Terms &amp; Conditions</li></ul></div>
    <div class="f-col" style="left:763px"><h4>Newsletter</h4></div>
    <div class="email">✉ Enter email address</div>
    <div class="subscribe">SUBSCRIBE</div>
    <div class="copyright">© 2022 <b>Zephyr Quill</b> All right reserved</div>
    <div class="cards"><span>Veyra</span><span>Mintcard</span><span>Maxo</span><span>Dyscan</span><span>Paywell</span></div>
  </footer>

</div>
</body>
</html>
```